Priority Goals poster for school year

We are an elementary school and the past two years have had you help us to design a "poster" that illustrates our goal of the coming year. I am attaching our last year's one, along with some photos of our (ver rough) thinking for next years. The priority goal at top remains the same. Can't wait to see your genius ideas! :)

Target Market(s)

Staff of an elementary school and parents to some (informative) extent as well.

Colors
296eb1
6094c6
fbed22
fbee3f

Requirements
Must have
• items from the white board picture we have attached

```html
<!DOCTYPE html>
<html lang="en">
<head>
<meta charset="utf-8">
<title>2020-2021 Priority Goals</title>
<link rel="stylesheet" href="https://fonts.googleapis.com/css2?family=Montserrat:wght@600;700;800&family=Oswald:wght@500;700&display=swap">
<style>
  :root {
    --blue-deep: #2b3a97;
    --blue: #296eb1;
    --blue-light: #6094c6;
    --yellow: #fbed22;
    --yellow-soft: #fbee3f;
    --yellow-deep: #f0c91b;
    --panel: #f2f1f3;
    --ink: #1d1d2b;
    --stage: #e8e8ea;
    --white: #ffffff;
  }
  * { margin: 0; padding: 0; box-sizing: border-box; }
  html, body { width: 1200px; height: 3060px; overflow: hidden; }
  body { background: var(--stage); font-family: 'Montserrat', sans-serif; position: relative; }

  .poster {
    position: absolute; left: 46px; top: 762px;
    width: 692px; height: 960px;
    background: var(--white);
    transform: scale(1.6); transform-origin: top left;
    box-shadow: 0 2px 10px rgba(0,0,0,.12);
    overflow: hidden;
  }
  .abs { position: absolute; }

  .year {
    left: 56px; top: 12px;
    font-family: 'Oswald', sans-serif; font-weight: 500;
    font-size: 76px; line-height: 1; letter-spacing: -2px;
    color: var(--blue);
    transform: scaleX(0.88); transform-origin: left top;
    white-space: nowrap;
  }
  .year .light { color: var(--blue-light); }
  .year .dash { color: var(--blue-deep); }

  .goals-title {
    left: 351px; top: 20px;
    font-weight: 800; font-size: 35px; line-height: 35px; letter-spacing: 0.5px;
  }
  .goals-title .priority { color: var(--yellow-deep); display: block; }
  .goals-title .goals { color: var(--blue-deep); display: block; }

  .school-name {
    left: 548px; top: 22px; width: 104px;
    font-weight: 800; font-size: 15px; line-height: 17px;
    color: var(--blue-deep); text-align: center;
  }

  .band {
    left: 0; top: 98px; width: 692px; height: 59px;
    background: var(--blue-deep);
  }
  .band .voices {
    position: absolute; left: 45px; top: 9px;
    font-weight: 800; font-size: 37px; line-height: 40px; color: var(--white);
  }
  .band .voices .all { color: var(--yellow); }
  .band .questions {
    position: absolute; left: 326px; top: 4px;
    font-weight: 800; font-size: 22px; line-height: 26px; color: var(--white);
  }

  .panel {
    left: 44px; top: 188px; width: 606px; height: 455px;
    background: var(--panel);
  }
  .diagram { left: 0; top: 0; width: 692px; height: 960px; }

  .label {
    font-weight: 700; font-size: 12.5px; line-height: 14px; color: var(--ink);
  }
  .label .lead-blue { color: var(--blue-light); }
  .label .lead-deep { color: var(--blue-deep); }
  .label .lead-yellow { color: var(--yellow-deep); }
  .label-top { left: 311px; top: 202px; }
  .label-left { left: 57px; top: 434px; }
  .label-right { left: 513px; top: 445px; }

  .center-name {
    left: 286px; top: 404px; width: 120px;
    font-weight: 800; font-size: 13px; line-height: 15px;
    color: var(--blue-deep); text-align: center;
  }

  .focus-row { left: 42px; top: 663px; width: 606px; height: 67px; display: flex; gap: 3px; }
  .focus-item {
    flex: 1; height: 67px; background: var(--yellow);
    display: flex; align-items: flex-start; gap: 7px;
    padding: 12px 8px 0 12px;
    font-weight: 700; font-size: 10px; line-height: 11.5px; color: var(--ink);
  }
  .focus-item:nth-child(odd) { background: var(--yellow-deep); }
  .focus-item svg { flex: none; width: 13px; height: 13px; margin-top: 1px; }

  .foundational {
    left: 0; top: 756px; width: 692px; text-align: center;
    font-family: 'Oswald', sans-serif; font-weight: 700;
    font-size: 72px; line-height: 72px; letter-spacing: -1px;
    color: var(--blue-deep);
  }
  .tagline {
    left: 0; top: 834px; width: 692px; text-align: center;
    font-weight: 800; font-size: 24px; line-height: 28px; color: var(--ink);
  }

  .footer-bg { left: 0; top: 883px; width: 692px; height: 77px; }
  .contact-main {
    left: 56px; top: 891px;
    font-weight: 700; font-size: 21px; line-height: 26px; color: var(--white);
  }
  .contact-main div, .contact-side div { display: flex; align-items: center; gap: 12px; }
  .contact-main svg { width: 18px; height: 18px; }
  .contact-side {
    left: 374px; top: 912px;
    font-weight: 700; font-size: 11.5px; line-height: 14px; color: var(--white);
    display: flex; align-items: center; gap: 10px;
  }
  .contact-side svg { width: 14px; height: 26px; }
</style>
</head>
<body>
<main class="poster">
  <div class="abs year"><span>20</span><span class="light">20</span><span class="dash">-</span><span>20</span><span class="light">21</span></div>
  <div class="abs goals-title"><span class="priority">PRIORITY</span><span class="goals">GOALS</span></div>
  <div class="abs school-name">CEDAR RIDGE ELEMENTARY</div>

  <section class="abs band">
    <div class="voices">Voices of <span class="all">ALL</span></div>
    <div class="questions">WHO ARE WE?<br>WHERE ARE WE GOING?</div>
  </section>

  <div class="abs panel"></div>

  <svg class="abs diagram" viewBox="0 0 692 960" aria-hidden="true">
    <g fill="none" stroke="var(--blue-deep)" stroke-width="3" stroke-linecap="round">
      <path d="M136 425 A210 210 0 0 1 291.6 222.2"/>
      <path d="M417.8 227.7 A210 210 0 0 1 556 425"/>
      <path d="M536.3 513.7 A210 210 0 0 1 160.6 523.6"/>
    </g>
    <g fill="var(--white)" stroke-width="3.5">
      <circle cx="291.6" cy="222.2" r="7" stroke="var(--blue-light)"/>
      <circle cx="417.8" cy="227.7" r="7" stroke="var(--blue-light)"/>
      <circle cx="136" cy="425" r="7" stroke="var(--blue-deep)"/>
      <circle cx="160.6" cy="523.6" r="7" stroke="var(--blue-deep)"/>
      <circle cx="556" cy="425" r="7" stroke="var(--yellow)"/>
      <circle cx="536.3" cy="513.7" r="7" stroke="var(--yellow)"/>
    </g>

    <g transform="translate(346 425)">
      <path d="M0 0 L-138.1 -37 A143 143 0 0 1 123.8 -71.5 Z" fill="var(--blue-light)"/>
      <path d="M0 0 L123.8 -71.5 A143 143 0 0 1 0 143 Z" fill="var(--yellow)"/>
      <path d="M0 0 L0 143 A143 143 0 0 1 -138.1 -37 Z" fill="var(--blue-deep)"/>
      <circle r="68" fill="var(--white)"/>

      <g transform="translate(0 -105)" fill="none" stroke="var(--white)" stroke-width="3.5">
        <circle r="17"/><circle r="10"/><circle r="3" fill="var(--white)"/>
        <path d="M2 -2 L16 -16 M12 -18 L18 -18 L18 -12" stroke-width="3"/>
      </g>
      <g transform="translate(-100 42)" fill="var(--white)">
        <rect x="-22" y="-10" width="8" height="20" rx="1"/>
        <rect x="14" y="-10" width="8" height="20" rx="1"/>
        <path d="M-14 -6 L-4 -10 L6 -4 L14 -6 L14 6 L6 12 L-2 10 L-14 4 Z"/>
      </g>
      <g transform="translate(95 40)" fill="none" stroke="var(--white)" stroke-width="3">
        <path d="M-16 -14 H14 V6 H-4 L-12 14 V6 H-16 Z"/>
        <path d="M-10 -6 H8 M-10 0 H4"/>
      </g>

      <circle cx="0" cy="-145" r="8" fill="#cfd0d6" stroke="var(--white)" stroke-width="3"/>
      <circle cx="-124" cy="75" r="9" fill="#cfd0d6" stroke="var(--blue-deep)" stroke-width="4"/>
      <circle cx="129" cy="63" r="8" fill="#dcdce0" stroke="var(--white)" stroke-width="3"/>
    </g>
  </svg>

  <div class="abs center-name">CEDAR RIDGE ELEMENTARY</div>

  <div class="abs label label-top"><span class="lead-blue">SMALL<br>MEASURRED</span><br>STEP TOWARDS<br>HIGER GOAL</div>
  <div class="abs label label-left"><span class="lead-deep">BUILD VALUE</span><br>PARTNERSHIPS<br>CONNECT, CELEBRATE<br>STRONG,PREDICTIONS<br>LAUGH, HAVE FUN</div>
  <div class="abs label label-right"><span class="lead-yellow">COMMUNICATE!</span><br>EYPECTAHARE<br>SUPPORT<br>FAR CLARITY</div>

  <div class="abs focus-row">
    <div class="focus-item"><svg viewBox="0 0 14 14"><circle cx="7" cy="7" r="7" fill="var(--blue-deep)"/><path d="M4 7.2 L6.2 9.3 L10 5" fill="none" stroke="var(--white)" stroke-width="1.8"/></svg><span>Be intentional<br>with padr actor-<br>focus</span></div>
    <div class="focus-item"><svg viewBox="0 0 14 14"><circle cx="7" cy="7" r="7" fill="var(--blue-deep)"/><path d="M4 7.2 L6.2 9.3 L10 5" fill="none" stroke="var(--white)" stroke-width="1.8"/></svg><span>Staff douing what<br>they love teaching</span></div>
    <div class="focus-item"><svg viewBox="0 0 14 14"><circle cx="7" cy="7" r="7" fill="var(--blue-deep)"/><path d="M4 7.2 L6.2 9.3 L10 5" fill="none" stroke="var(--white)" stroke-width="1.8"/></svg><span>Mental health<br>wellness for every<br>person in out<br>school community</span></div>
    <div class="focus-item"><svg viewBox="0 0 14 14"><circle cx="7" cy="7" r="7" fill="var(--blue-deep)"/><path d="M4 7.2 L6.2 9.3 L10 5" fill="none" stroke="var(--white)" stroke-width="1.8"/></svg><span>Broken<br>over leas</span></div>
  </div>

  <h1 class="abs foundational">FOUNDATIONAL</h1>
  <div class="abs tagline">(4 YEARS STRONG, BETTER EVERYDAT)</div>

  <svg class="abs footer-bg" viewBox="0 0 692 77" aria-hidden="true">
    <path d="M338 17 H692 V77 H366 Z" fill="var(--blue-light)"/>
    <path d="M0 0 H318 L366 77 H0 Z" fill="var(--blue-deep)"/>
  </svg>

  <div class="abs contact-main">
    <div><svg viewBox="0 0 20 20"><path d="M5 2 L8 6 L6 8 C7 11 9 13 12 14 L14 12 L18 15 L16 18 C9 18 2 11 2 4 Z" fill="none" stroke="var(--white)" stroke-width="1.8"/></svg>555-014-2200</div>
    <div><svg viewBox="0 0 20 20"><rect x="2" y="5" width="16" height="11" fill="none" stroke="var(--white)" stroke-width="1.8"/><path d="M2 5 L10 11 L18 5" fill="none" stroke="var(--white)" stroke-width="1.8"/></svg>@cedarridgelearner</div>
  </div>

  <div class="abs contact-side">
    <svg viewBox="0 0 14 26"><circle cx="7" cy="5" r="4.5" fill="none" stroke="var(--white)" stroke-width="1.3"/><path d="M2.5 5 H11.5 M7 0.5 V9.5" stroke="var(--white)" stroke-width="1"/><path d="M7 24 C3 19 3 17 3 16 A4 4 0 0 1 11 16 C11 17 11 19 7 24 Z" fill="none" stroke="var(--white)" stroke-width="1.3"/></svg>
    <span>cedarridge.example.org<br>1820 Birch Lane, Pine Hollow, WA 98000</span>
  </div>
</main>
</body>
</html>
```